Women's Online Clothing Boutique Needs Business Cards

I already have a logo that I would like to use. Some of the things that interest me is black business cards, foil embossed logo, glossy embossed logo, leopard print, no yellow font, rounded edges. I even like just a large logo on the front side with all of my information on the back side.

Contact Information for Business Card

https://copperfinch.shopvendly.example/
https://www.friendloop.example/thecopperfinchboutique/
https://www.snapgrid.example/thecopperfinchboutique/
copperfinchboutique@mailora.example

Requirements
Must have
• My Logo
Nice to have
• Leopard Print
Should not have
• No Yellow Font

```html
<!DOCTYPE html>
<html lang="en">
<head>
<meta charset="utf-8">
<title>The Copper Finch Boutique – Business Card</title>
<link rel="stylesheet" href="https://fonts.googleapis.com/css2?family=Arimo:wght@400&display=swap">
<style>
  :root {
    --backdrop: #3a3a3a;
    --card-black: #1c1c1c;
    --ink-black: #0a0a0a;
    --card-white: #f4f4f2;
    --gold: #c4952c;
    --text-grey: #4a4a4a;
  }
  * { margin: 0; padding: 0; box-sizing: border-box; }
  html, body {
    width: 1200px;
    height: 1015px;
    overflow: hidden;
    background: var(--backdrop);
    font-family: "Arimo", Arial, sans-serif;
  }
  .sheet {
    width: 1200px;
    height: 1015px;
    display: flex;
    flex-direction: column;
    align-items: center;
    justify-content: center;
    gap: 56px;
  }
  .card {
    position: relative;
    width: 760px;
    height: 434px;
    border-radius: 14px;
    box-shadow: 0 10px 28px rgba(0,0,0,0.45);
  }
  .card--front { background: var(--card-black); }
  .card--back { background: var(--card-white); }

  .brand {
    position: absolute;
    display: flex;
    align-items: center;
    gap: 14px;
  }
  .brand__dot {
    width: 18px;
    height: 18px;
    border-radius: 50%;
    flex: none;
  }
  .brand__name {
    font-size: 44px;
    font-weight: 400;
    letter-spacing: 0.5px;
    white-space: nowrap;
  }
  .brand__rule {
    position: absolute;
    height: 1px;
  }

  .card--front .brand { left: 50%; top: 50%; transform: translate(-50%, -50%); }
  .card--front .brand__dot { background: var(--ink-black); }
  .card--front .brand__name { color: var(--ink-black); }
  .card--front .brand__rule { background: var(--ink-black); left: 170px; right: 170px; top: 262px; }

  .card--back .brand { right: 52px; top: 70px; }
  .card--back .brand__dot { background: var(--gold); }
  .card--back .brand__name { color: var(--gold); font-size: 38px; }
  .card--back .brand__rule { background: var(--gold); right: 52px; width: 430px; top: 130px; }

  .contact {
    position: absolute;
    left: 52px;
    bottom: 54px;
    list-style: none;
    color: var(--text-grey);
    font-size: 19px;
  }
  .contact__item {
    display: flex;
    align-items: center;
    gap: 12px;
    line-height: 30px;
    white-space: nowrap;
  }
  .contact__item--gap { margin-top: 22px; }
  .contact__icon { width: 20px; height: 20px; flex: none; }
  .contact__icon--social {
    width: 18px;
    height: 18px;
    margin: 0 1px;
    border-radius: 3px;
    background: var(--gold);
  }
</style>
</head>
<body>
<main class="sheet">
  <section class="card card--front" aria-label="Business card front">
    <div class="brand">
      <span class="brand__dot"></span>
      <span class="brand__name">The Copper Finch Boutique</span>
    </div>
    <span class="brand__rule"></span>
  </section>

  <section class="card card--back" aria-label="Business card back">
    <div class="brand">
      <span class="brand__dot"></span>
      <span class="brand__name">The Copper Finch Boutique</span>
    </div>
    <span class="brand__rule"></span>

    <ul class="contact">
      <li class="contact__item">
        <svg class="contact__icon" viewBox="0 0 20 20" aria-hidden="true">
          <rect x="1" y="4" width="18" height="12" fill="var(--gold)"/>
          <path d="M1 4 L10 11 L19 4" fill="none" stroke="#fff" stroke-width="1.5"/>
        </svg>
        <span>copperfinchboutique@mailora.example</span>
      </li>
      <li class="contact__item">
        <svg class="contact__icon" viewBox="0 0 20 20" aria-hidden="true">
          <circle cx="10" cy="10" r="9" fill="var(--gold)"/>
          <g fill="none" stroke="#fff" stroke-width="1.1">
            <ellipse cx="10" cy="10" rx="4" ry="9"/>
            <line x1="1" y1="10" x2="19" y2="10"/>
            <line x1="10" y1="1" x2="10" y2="19"/>
          </g>
        </svg>
        <span>www.copperfinch.shopvendly.example</span>
      </li>
      <li class="contact__item contact__item--gap">
        <span class="contact__icon contact__icon--social"></span>
        <span>www.friendloop.example/thecopperfinchboutique</span>
      </li>
      <li class="contact__item">
        <span class="contact__icon contact__icon--social"></span>
        <span>www.snapgrid.example/thecopperfinchboutique</span>
      </li>
    </ul>
  </section>
</main>
</body>
</html>
```